KVR Associates needs a web site

We need a web site for www.kvrassociates-example.com. KVR is a mergers and acquisition consulting company that focuses our buyer and seller services on logistics companies. We help put companies together, and help with legal and financial due diligence. We want the web site to express our service and show the logistics components. We want personalized images versus pictures of trucks and airplanes.

Our new logo uses Burgandy and grey colors. Image attached. We are not in to bold, big letters...classy, artistic, low key preferred. Confidentiality, experience, professional are what we want to express on the site.

All we expect for the first part of this project is a home page, and one subpage.  We are budgeting other funds for the technical aspects of the web site

Reason: All that I'm seeing so far is trucks, forklifts and planes. We are a legal mergers and acquisitions firm that focus on logistics. I like some of the images to say logistics, but really want it say legal, financial, and putting companies together. Will pay extra for the sub page if someone can impress us with a home page.

Reason: Swamped with another project at the moment...will work on this over the weekend and provide designer feedback and select final design by Tuesday

```html
<!DOCTYPE html>
<html lang="en">
<head>
<meta charset="utf-8">
<title>KVR Associates</title>
<link href="https://fonts.googleapis.com/css2?family=Arimo:wght@400;700&display=swap" rel="stylesheet">
<style>
:root{
  --burgundy:#b4002f;
  --charcoal:#4b4b4b;
  --slate:#5c5d5f;
  --heading:#4a4a4a;
  --text:#8e8e8e;
  --light:#ececec;
  --field:#ebebeb;
  --rule:#dcdcdc;
  --white:#ffffff;
}
*{box-sizing:border-box;margin:0;padding:0}
html,body{width:911px;height:1200px;overflow:hidden;background:var(--white);font-family:"Arimo",Arial,sans-serif;color:var(--text)}
.page{position:relative;width:911px;height:1200px}
.abs{position:absolute}

.topbar{left:0;top:0;width:911px;height:18px;background:var(--charcoal);color:var(--white);font-size:10px}
.topbar .item{position:absolute;top:3px;display:flex;align-items:center;gap:6px}
.topbar svg{width:13px;height:13px}

.brand{left:120px;top:44px;font-size:24px;color:var(--heading);letter-spacing:.5px;display:flex;align-items:center;gap:8px}
.brand .mark{width:12px;height:12px;background:var(--burgundy)}

.nav{left:406px;top:34px;height:42px;display:flex}
.nav a{display:flex;align-items:center;justify-content:center;height:42px;color:var(--white);text-decoration:none;font-size:10.5px}
.nav .active{background:var(--burgundy)}
.nav .plain{background:var(--slate)}

.hero{left:0;top:91px;width:911px;height:333px;
  background:
    radial-gradient(ellipse 120px 110px at 790px 250px,#3a3a3a 0%,#6e6e6e 55%,rgba(110,110,110,0) 100%),
    radial-gradient(ellipse 90px 80px at 660px 230px,#505050 0%,#8a8a8a 60%,rgba(138,138,138,0) 100%),
    radial-gradient(ellipse 130px 90px at 500px 290px,#3e3e3e 0%,#777 55%,rgba(119,119,119,0) 100%),
    radial-gradient(ellipse 200px 120px at 150px 300px,#505050 0%,#888 55%,rgba(136,136,136,0) 100%),
    radial-gradient(ellipse 90px 40px at 700px 40px,#4a4a4a 0%,rgba(74,74,74,0) 100%),
    linear-gradient(180deg,#9d9d9d 0%,#c4c4c4 55%,#bcbcbc 78%,#8f8f8f 100%)}
.hero-title{left:144px;top:240px;color:var(--white)}
.hero-title .small{font-size:15px;display:block}
.hero-title .big{font-size:22px;font-weight:700;color:#5e5e5e;margin-top:6px;display:block}
.hero-title .big em{font-style:normal;color:var(--burgundy)}

.about{left:0;top:424px;width:911px;height:81px;background:var(--light)}
.section-title{font-size:17px;font-weight:700;color:var(--heading)}
.section-title em{font-style:normal;color:var(--burgundy)}
.about .section-title{position:absolute;left:119px;top:9px}
.about p{position:absolute;left:119px;top:33px;width:580px;font-size:9px;line-height:12px;color:#9a9a9a}

.btn-red{background:var(--burgundy);color:var(--white);font-size:9px;display:flex;align-items:center;justify-content:center}
.btn-dark{background:var(--slate);color:var(--white);font-size:9px;display:flex;align-items:center;justify-content:center;border-bottom:3px solid var(--burgundy)}

.services-title{left:119px;top:524px}
.card{top:551px;width:218px;height:140px;border:1px solid var(--rule);padding:6px}
.card .photo{width:100%;height:100%}
.card-title{top:700px;width:218px;font-size:9.5px;font-weight:700;color:var(--heading)}
.card-text{top:722px;width:218px;font-size:9.5px;line-height:11.6px;text-align:justify}
.card-btn{top:842px;width:62px;height:30px}

.divider{left:119px;top:884px;width:674px;height:1px;background:var(--rule)}

.form-label{font-size:9.5px;color:var(--heading)}
.field{background:var(--field);border:1px solid #cfcfcf;font-size:9.5px;font-style:italic;color:#b0b0b0;padding:5px}

.map{left:426px;top:930px;width:367px;height:160px;
  background:
    radial-gradient(ellipse 60px 40px at 190px 70px,#f6d9a6 0%,rgba(246,217,166,0) 100%),
    radial-gradient(ellipse 90px 50px at 80px 120px,#d8e4c8 0%,rgba(216,228,200,0) 100%),
    radial-gradient(ellipse 80px 50px at 300px 40px,#e2e8d6 0%,rgba(226,232,214,0) 100%),
    linear-gradient(135deg,#ebe7dc 0%,#f2efe7 50%,#e3e9da 100%)}

.footer-line{left:0;top:1117px;width:911px;height:2px;background:var(--burgundy)}
.footer-head{font-size:11px;font-weight:700;color:var(--heading)}
.footer-links{display:flex;gap:22px;font-size:7px;color:var(--heading)}
.footer-small{font-size:7px;color:var(--text)}
.vrule{width:1px;background:var(--rule);top:1128px;height:60px}
.footer-contact{font-size:9px;line-height:12px;color:var(--text)}
.footer-brand{left:636px;top:1145px;font-size:20px;color:var(--heading);display:flex;align-items:center;gap:7px}
.footer-brand .mark{width:10px;height:10px;background:var(--burgundy)}
</style>
</head>
<body>
<div class="page">

  <div class="abs topbar">
    <div class="item" style="left:522px">
      <svg viewBox="0 0 16 16" aria-hidden="true"><circle cx="8" cy="8" r="7" fill="none" stroke="#fff" stroke-width="1.2"/><path d="M5.5 4.5l1.5 0 .6 2-1 .8a5 5 0 0 0 2.2 2.2l.8-1 2 .6v1.5c-3.5.5-6.6-2.6-6.1-6.1z" fill="#fff"/></svg>
      <span>555.014.2630</span>
    </div>
    <div class="item" style="left:640px">
      <svg viewBox="0 0 16 16" aria-hidden="true"><circle cx="8" cy="8" r="7" fill="none" stroke="#fff" stroke-width="1.2"/><rect x="4" y="5.5" width="8" height="5.5" fill="none" stroke="#fff" stroke-width="1"/><path d="M4 5.5l4 3 4-3" fill="none" stroke="#fff" stroke-width="1"/></svg>
      <span>contact@kvrassociates-example.com</span>
    </div>
  </div>

  <div class="abs brand"><span>KVR Associates</span><span class="mark"></span></div>

  <nav class="abs nav">
    <a class="active" style="width:76px">Home</a>
    <a class="plain" style="width:80px">Services</a>
    <a class="plain" style="width:74px">Clients</a>
    <a class="plain" style="width:79px">About</a>
    <a class="active" style="width:77px">Contact</a>
  </nav>

  <div class="abs hero" role="img" aria-label="Greyscale banner: cargo ship, container truck, airplane and globes over a world map"></div>
  <div class="abs hero-title">
    <span class="small">WELCOME TO</span>
    <span class="big">KVR <em>ASSOCIATES</em></span>
  </div>

  <section class="abs about">
    <h2 class="section-title">ABOUT <em>US</em></h2>
    <p>KVR assists business owners within the logistics industry to implement growth and exit strategies. We offer business planning and merger and acquisition(M&amp;A) advisory services. KVR services are offered by industry executives with extensive M&amp;A experience. Your company will benefit from a unique and outside perspective from consultants that understand your business.</p>
    <div class="abs btn-red" style="left:731px;top:33px;width:62px;height:29px">Read More</div>
  </section>

  <h2 class="abs section-title services-title">SERVICES</h2>

  <div class="abs card" style="left:119px"><div class="photo" role="img" aria-label="Container ship at sea" style="background:radial-gradient(ellipse 70px 40px at 90px 60px,#8a3b3b 0%,#3d5a7a 55%,rgba(61,90,122,0) 100%),linear-gradient(180deg,#c9dbe9 0%,#7da6c8 30%,#3f78aa 65%,#1f4b78 100%)"></div></div>
  <div class="abs card" style="left:347px"><div class="photo" role="img" aria-label="Cargo airplane on the tarmac at sunset" style="background:radial-gradient(ellipse 90px 35px at 120px 55px,#d8d6d0 0%,#b7ab95 55%,rgba(183,171,149,0) 100%),radial-gradient(ellipse 40px 30px at 25px 40px,#fff2c8 0%,rgba(255,242,200,0) 100%),linear-gradient(180deg,#f3d9a0 0%,#d9b47a 45%,#8f7860 75%,#4e4238 100%)"></div></div>
  <div class="abs card" style="left:575px"><div class="photo" role="img" aria-label="Green truck on a highway under a blue sky" style="background:radial-gradient(ellipse 70px 40px at 110px 85px,#1f6b5c 0%,#2f5e55 50%,rgba(47,94,85,0) 100%),radial-gradient(ellipse 50px 60px at 170px 60px,#c87a55 0%,rgba(200,122,85,0) 100%),linear-gradient(180deg,#2f67a8 0%,#7fa8d0 45%,#8c8a84 75%,#4e5450 100%)"></div></div>

  <div class="abs card-title" style="left:119px">LOREM IPSUM TEXT EXAMPLE</div>
  <div class="abs card-title" style="left:347px">LOREM IPSUM TEXT EXAMPLE</div>
  <div class="abs card-title" style="left:575px">LOREM IPSUM TEXT EXAMPLE</div>

  <p class="abs card-text" style="left:119px">Lorem ipsum dolor sit amet, consectetur adipisicing elit, sed do eiusmod tempor incididunt ut labore et dolore magna aliqua. Ut enim ad minim veniam, quis nostrud exercitation ullamco laboris nisi ut aliquip ex ea commodo consequat. Duis aute irure dolor in reprehenderit in voluptate velit esse cillum dolore eu fugiat nulla pariatur. Excepteur sint occaecat cupidatat non proident, sunt in culpa qui officia deserunt mollit anim id est laborum</p>
  <p class="abs card-text" style="left:347px">Lorem ipsum dolor sit amet, consectetur adipisicing elit, sed do eiusmod tempor incididunt ut labore et dolore magna aliqua. Ut enim ad minim veniam, quis nostrud exercitation ullamco laboris nisi ut aliquip ex ea commodo consequat. Duis aute irure dolor in reprehenderit in voluptate velit esse cillum dolore eu fugiat nulla pariatur. Excepteur sint occaecat cupidatat non proident, sunt in culpa qui officia deserunt mollit anim id est laborum</p>
  <p class="abs card-text" style="left:575px">Lorem ipsum dolor sit amet, consectetur adipisicing elit, sed do eiusmod tempor incididunt ut labore et dolore magna aliqua. Ut enim ad minim veniam, quis nostrud exercitation ullamco laboris nisi ut aliquip ex ea commodo consequat. Duis aute irure dolor in reprehenderit in voluptate velit esse cillum dolore eu fugiat nulla pariatur. Excepteur sint occaecat cupidatat non proident, sunt in culpa qui officia deserunt mollit anim id est laborum</p>

  <div class="abs btn-dark card-btn" style="left:275px">Read More</div>
  <div class="abs btn-dark card-btn" style="left:503px">Read More</div>
  <div class="abs btn-dark card-btn" style="left:731px">Read More</div>

  <div class="abs divider"></div>

  <h2 class="abs section-title" style="left:119px;top:903px">CONTACT <em>US</em></h2>
  <span class="abs form-label" style="left:118px;top:929px">Name:</span>
  <span class="abs form-label" style="left:269px;top:929px">Email:</span>
  <div class="abs field" style="left:118px;top:942px;width:142px;height:29px">Enter Name</div>
  <div class="abs field" style="left:269px;top:942px;width:143px;height:29px">Enter Email</div>
  <span class="abs form-label" style="left:118px;top:981px">Message:</span>
  <div class="abs field" style="left:118px;top:994px;width:294px;height:55px">Enter Your Message</div>
  <div class="abs btn-dark" style="left:349px;top:1060px;width:63px;height:30px">Submit</div>

  <h2 class="abs section-title" style="left:431px;top:903px">LOCATE <em>US</em></h2>
  <div class="abs map" role="img" aria-label="Street map showing the office location"></div>

  <div class="abs footer-line"></div>

  <h3 class="abs footer-head" style="left:119px;top:1129px">SITEMAP</h3>
  <div class="abs footer-links" style="left:119px;top:1148px"><span>HOME</span><span>SERVICE</span><span>CLIENTS</span><span>ABOUT</span><span>CONTACT</span></div>
  <p class="abs footer-small" style="left:119px;top:1166px">Copyright © 2014 KVR Associates, LLC. All Rights Reserved.</p>

  <div class="abs vrule" style="left:382px"></div>

  <h3 class="abs footer-head" style="left:412px;top:1129px">CONTACT</h3>
  <div class="abs footer-contact" style="left:412px;top:1144px">
    P.O Box 4120 Maple Grove, IL 60199<br>555.014.2630<br>contact@kvrassociates-example.com
  </div>

  <div class="abs vrule" style="left:606px"></div>

  <div class="abs footer-brand"><span>KVR Associates</span><span class="mark"></span></div>

</div>
</body>
</html>
```